Banner Ad Design Project

We are re-branding our energy management company called 'Voltrix'. We sell Energy Management Information Software and are currently positioned as a very technical organization. While we are always going to be very technical we want to shift away from telling people about the power of our software and become a more customer centric organization focusing on how energy management can solve many of your organizations problems. The final design should be modern and simple, as we are taking something very technical and complicated and trying to sell it. We need 4 banners created for our site www.voltrix-example.com which rotate across the top. They all need to be different and easily editable (preferably Photoshop)as we change marketing campaigns, the text needs to be editable.

The Size of the banners are 940 pixels by 250 pixels.
Updates

Thank you so much to everyone for you questions and for the few designs I have received. I am very new at this so please if there are things I can do to help better convey my design needs please let me know. Many people have asked for the Text to do on the banners. Here is what I have come up with for the 4 banners.

Banner 1

Maintain high building standards
                - With lower energy costs

Banner 2
Energy Reporting Requirements
                - Made effortless

Banner 3
Presenting Colin Parsons, President of RDLMS, June 19th
- The future of Ontario’s power market

Banner 4
Working with utilities to develop and execute successful Energy Conservation Programs

As well we are working on re-branding ourselves so the website at this point does not convey the look and feel we are looking to go with. The attached files, especially the brochure and business card, convey the look and feel I am looking fore much better!

Reason: Need to check with the rest of my team to make final decision. Keep submitting designs, Thanks!

Industry/Entity Type

Marketing

Requirements
Must have
• The size needs to be 940 by 250 pixels. They need to contain the green color indicated in the 'Voltrix branding design features' document.

Needs to be consistent withe the look and feel of the brochure, PowerPoint and business card attached.

The integration of the 'Voltrix Head' and other similar graphics into the banners.
Should not have
• The look and feel of our current website

```html
<!DOCTYPE html>
<html lang="en">
<head>
<meta charset="utf-8">
<title>Voltrix Rotating Banners</title>
<link rel="stylesheet" href="https://fonts.googleapis.com/css2?family=Arvo:wght@700&family=Raleway:wght@300&display=swap">
<style>
  :root {
    --green-dark: #00582f;
    --green-lime: #8dc63f;
    --panel-bg: #efefef;
    --page-bg: #ffffff;
    --art-soft: #cfe1c4;
  }
  * { box-sizing: border-box; margin: 0; padding: 0; }
  html, body {
    width: 1200px;
    height: 1000px;
    overflow: hidden;
    background: var(--page-bg);
  }
  .banner-stack {
    position: relative;
    width: 1200px;
    height: 1000px;
  }
  .banner {
    position: absolute;
    left: 224px;
    width: 752px;
    height: 200px;
    background: var(--panel-bg);
    overflow: hidden;
  }
  .banner--building { top: 58px; }
  .banner--reporting { top: 288px; }
  .banner--speaker { top: 518px; }
  .banner--conservation { top: 748px; }

  .banner__copy {
    position: absolute;
    left: 32px;
    top: 24px;
    width: 476px;
    border-top: 1px dashed var(--green-dark);
    border-bottom: 1px dashed var(--green-dark);
    padding: 10px 0 14px;
  }
  .banner__headline {
    font-family: "Arvo", "Rockwell", serif;
    font-weight: 700;
    font-size: 26.6px;
    line-height: 30px;
    color: var(--green-dark);
    white-space: nowrap;
  }
  .banner__headline--two-line { line-height: 29px; }
  .banner__headline sup {
    font-size: 13px;
    vertical-align: 11px;
    line-height: 0;
  }
  .banner__tagline {
    font-family: "Raleway", "Helvetica Neue", sans-serif;
    font-weight: 300;
    font-size: 22px;
    line-height: 24px;
    letter-spacing: 0.3px;
    color: var(--green-lime);
    text-align: right;
    white-space: nowrap;
  }
  .banner--reporting .banner__tagline { padding-right: 19px; }
  .banner--speaker .banner__tagline { padding-right: 51px; }
  .banner--conservation .banner__tagline { padding-right: 42px; }

  .banner__art {
    position: absolute;
  }
  .banner--building .banner__art {
    left: 558px; top: 24px; width: 140px; height: 143px;
    background: var(--green-dark);
  }
  .banner--reporting .banner__art {
    left: 558px; top: 24px; width: 144px; height: 154px;
    background: var(--green-dark);
  }
  .banner--speaker .banner__art {
    left: 548px; top: 24px; width: 167px; height: 162px;
    background: var(--green-dark);
  }
  .banner--conservation .banner__art {
    left: 556px; top: 24px; width: 140px; height: 176px;
    background: linear-gradient(180deg, var(--green-lime), var(--art-soft));
  }
</style>
</head>
<body>
<main class="banner-stack">

  <section class="banner banner--building">
    <div class="banner__copy">
      <h2 class="banner__headline">Maintain high building standards</h2>
      <p class="banner__tagline">With lower energy costs</p>
    </div>
    <div class="banner__art" role="img" aria-label="Illustration of energy icons linked by dashed lines to a large institutional building"></div>
  </section>

  <section class="banner banner--reporting">
    <div class="banner__copy">
      <h2 class="banner__headline">Energy Reporting Requirements</h2>
      <p class="banner__tagline">Made effortless</p>
    </div>
    <div class="banner__art" role="img" aria-label="Illustration of renewable energy icons feeding into a report panel with charts"></div>
  </section>

  <section class="banner banner--speaker">
    <div class="banner__copy">
      <h2 class="banner__headline banner__headline--two-line">Presenting Colin Parsons,<br>President of RDLMS, June 19<sup>th</sup></h2>
      <p class="banner__tagline">The future of Ontario’s power market</p>
    </div>
    <div class="banner__art" role="img" aria-label="Map of Ontario with power transmission towers"></div>
  </section>

  <section class="banner banner--conservation">
    <div class="banner__copy">
      <h2 class="banner__headline banner__headline--two-line">Working with utilities to develop<br>and execute successful Energy</h2>
      <p class="banner__tagline">Conservation Programs</p>
    </div>
    <div class="banner__art" role="img" aria-label="Line illustration of a head in profile with a light bulb, topped by resource icons"></div>
  </section>

</main>
</body>
</html>
```